Appraisal and Umpire Services for Property Damage Insurance Claims

I need a banner design that I can post as an advertisement on industry web pages. I would like this to be elegant and reflective of quality, integrity and professionalism.

Target Market(s)

Insurance Companies and Attorneys

Industry/Entity Type

Insurance

Contact Information for Business Card

Gerald M. Hollis
918 Birchwell Lane
PO Box 582
Clifton Park, NY 12093
ghollis@brindlevault.com
Phone: (800) 555-0147, Ext. 2861
Direct: (315) 555-0189

Logo Text

Line One: Velmar Brook Claim Service, Inc. Line two: Appraisal and Umpire Services

Font styles to use
Serif
Sans Serif

Colors
0255a3
f78f20
faa54b
3176b5

Requirements
Must have
• New Logo and matching banner, business card and stationary.
• The colors must be orange and navy blue in the logo. I have selected them below.

```html
<!DOCTYPE html>
<html lang="en">
<head>
<meta charset="utf-8">
<title>Velmar Brook Claim Service – Appraisal and Umpire Banner</title>
<link rel="stylesheet" href="https://fonts.googleapis.com/css2?family=Open+Sans:wght@300;400&family=Ubuntu:wght@500;700&display=swap">
<style>
  :root {
    --page-bg: #2b2b2d;
    --banner-bg: #f3f4f6;
    --orange: #f47a2a;
    --orange-light: #faa54b;
    --navy: #272b66;
    --text-grey: #4a4a4e;
    --white: #ffffff;
    --brick: #8a5a4c;
    --char: #2f3540;
  }
  html, body {
    margin: 0;
    width: 1200px;
    height: 1200px;
    overflow: hidden;
    background: var(--page-bg);
  }
  .banner-frame {
    position: absolute;
    left: 40px;
    top: 283px;
    width: 1120px;
    height: 633px;
    overflow: hidden;
  }
  .banner {
    position: relative;
    width: 1318px;
    height: 745px;
    transform: scale(0.85);
    transform-origin: 0 0;
    background: linear-gradient(180deg, #ffffff 0%, var(--banner-bg) 100%);
    font-family: "Open Sans", sans-serif;
  }
  .photo-area {
    position: absolute;
    inset: 0;
    width: 1318px;
    height: 745px;
  }
  .brand {
    position: absolute;
    left: 110px;
    top: 55px;
    display: flex;
    align-items: center;
    gap: 22px;
  }
  .brand-dot {
    width: 110px;
    height: 110px;
    border-radius: 50%;
    background: var(--orange);
  }
  .brand-name {
    font-family: "Ubuntu", sans-serif;
    font-weight: 500;
    color: var(--navy);
    font-size: 54px;
    line-height: 1;
    letter-spacing: -1px;
  }
  .brand-tagline {
    font-family: "Ubuntu", sans-serif;
    font-weight: 500;
    color: var(--navy);
    font-size: 17px;
    letter-spacing: 5px;
    margin-top: 8px;
  }
  .service-band {
    position: absolute;
    left: 0;
    top: 210px;
    width: 740px;
    height: 60px;
    background: var(--orange);
    clip-path: polygon(0 0, 100% 0, 96% 100%, 0 100%);
  }
  .service-band h1 {
    margin: 0;
    padding-left: 48px;
    line-height: 60px;
    font-family: "Ubuntu", sans-serif;
    font-weight: 500;
    font-size: 40px;
    color: var(--white);
  }
  .service-list {
    position: absolute;
    left: 56px;
    top: 295px;
    width: 560px;
    margin: 0;
    padding: 0;
    list-style: none;
    display: grid;
    grid-template-columns: 322px 238px;
    row-gap: 22px;
  }
  .service-item {
    display: flex;
    align-items: flex-start;
    gap: 16px;
    font-weight: 300;
    font-size: 44px;
    line-height: 52px;
    color: var(--text-grey);
  }
  .service-icon {
    flex: none;
    width: 54px;
    height: 54px;
    margin-top: 0;
  }
  .contact-band {
    position: absolute;
    left: 0;
    top: 594px;
    width: 570px;
    height: 151px;
    background: var(--navy);
    clip-path: polygon(0 0, 100% 0, 91% 100%, 0 100%);
    color: var(--white);
  }
  .contact-label {
    position: absolute;
    left: 45px;
    top: 26px;
    font-weight: 300;
    font-size: 42px;
    letter-spacing: -1px;
    line-height: 1;
  }
  .contact-phone {
    position: absolute;
    left: 43px;
    top: 72px;
    font-family: "Ubuntu", sans-serif;
    font-weight: 700;
    font-size: 52px;
    line-height: 1;
  }
</style>
</head>
<body>
  <div class="banner-frame">
    <div class="banner">
      <svg class="photo-area" viewBox="0 0 1318 745" role="img" aria-label="Photograph of a fire-damaged red brick building with charred walls and broken windows">
        <defs>
          <linearGradient id="photoTone" x1="0" y1="0" x2="1" y2="0.4">
            <stop offset="0" stop-color="#9a7468"/>
            <stop offset="0.45" stop-color="var(--brick)"/>
            <stop offset="0.7" stop-color="var(--char)"/>
            <stop offset="1" stop-color="#6e4a40"/>
          </linearGradient>
        </defs>
        <polygon points="908,0 1318,0 1318,745 513,745" fill="url(#photoTone)"/>
      </svg>

      <div class="brand">
        <div class="brand-dot"></div>
        <div>
          <div class="brand-name">Velmar Brook</div>
          <div class="brand-tagline">CLAIM SERVICE, INC</div>
        </div>
      </div>

      <div class="service-band"><h1>Appraisal and Umpire Services</h1></div>

      <ul class="service-list">
        <li class="service-item">
          <svg class="service-icon" viewBox="0 0 54 54" aria-hidden="true"><circle cx="27" cy="27" r="27" fill="var(--orange)"/><path d="M13 33 l3-8 h22 l3 8 v5 h-28z" fill="var(--white)"/><circle cx="19" cy="38" r="3" fill="var(--orange)"/><circle cx="35" cy="38" r="3" fill="var(--orange)"/></svg>
          <span>Accidents</span>
        </li>
        <li class="service-item">
          <svg class="service-icon" viewBox="0 0 54 54" aria-hidden="true"><circle cx="27" cy="27" r="27" fill="var(--orange)"/><path d="M12 38 q4-5 8 0 t8 0 t8 0 t8 0" stroke="var(--white)" stroke-width="3" fill="none"/><path d="M17 30 l10-10 l10 10 v3 h-20z" fill="var(--white)"/></svg>
          <span>Flood</span>
        </li>
        <li class="service-item">
          <svg class="service-icon" viewBox="0 0 54 54" aria-hidden="true"><circle cx="27" cy="27" r="27" fill="var(--orange)"/><path d="M14 40 v-14 h8 v-8 h8 v22z M32 40 v-10 h8 v10z" fill="var(--white)"/></svg>
          <span>Disasters</span>
        </li>
        <li class="service-item">
          <svg class="service-icon" viewBox="0 0 54 54" aria-hidden="true"><circle cx="27" cy="27" r="27" fill="var(--orange)"/><path d="M13 22 h20 a5 5 0 1 0 -5 -5 M13 29 h26 a5 5 0 1 1 -5 5 M13 36 h14" stroke="var(--white)" stroke-width="3" fill="none" stroke-linecap="round"/></svg>
          <span>Wind</span>
        </li>
        <li class="service-item">
          <svg class="service-icon" viewBox="0 0 54 54" aria-hidden="true"><circle cx="27" cy="27" r="27" fill="var(--orange)"/><path d="M27 12 l14 12 h-4 v13 h-20 v-13 h-4z" fill="var(--white)"/><rect x="24" y="29" width="6" height="8" fill="var(--orange)"/></svg>
          <span>Property &amp;<br>Liability</span>
        </li>
        <li class="service-item">
          <svg class="service-icon" viewBox="0 0 54 54" aria-hidden="true"><circle cx="27" cy="27" r="27" fill="var(--orange)"/><path d="M27 11 c4 8 12 12 12 22 a12 12 0 0 1 -24 0 c0-6 4-9 6-12 c1 4 3 6 5 6 c0-6 -1-10 1-16z" fill="var(--white)"/></svg>
          <span>Fire</span>
        </li>
      </ul>

      <div class="contact-band">
        <div class="contact-label">CONTACT US TODAY</div>
        <div class="contact-phone">(800) 555-0147</div>
      </div>
    </div>
  </div>
</body>
</html>
```